New online business - used mobile phones - needs unique eye catching web design that sets it apart

The Handset Bazaar
We are a new business looking for a rapid response for our web site design. We don't want a normal website....... we need to be creative - most important PLEASE view the attached files uploaded 3 March to ensure you get us :)
.
The Handset Bazaar buys new and damaged mobile phones from the public. A simple process they complete to sell their mobile to us; we want our website to reflect this.
Our website needs to be modern, edgy and fun, not corporate and definitely not like any other mobile phone buying site in the world today!!
Our name was taken from a play on the share/stock market which we have tried to bring into the design ....... it hasn't worked with early designs submitted. Now taking a different approach. Refer to new attached files which should help you visualise our concept.

We like layout from Sketch Flock – rtlbenoviqs #7132809 design as this is very close to our layout vision.
The first page to tell the public what we do, how we do it, and then they click to accept the instant online quote. (page two they complete details about the mobiles model & condition they are selling, then page three complete their personal details).
Our background preference is dark, blackboard or dark with slight texture
a) We love white on black/dark background either typewriter font or look like hand drawn refer to attached files & heronandfig.com.au site to see. Would Label font work???

b) Where the light blue colour is on #7132809 this needs to be like chromavell colour classic green, fern green or bright green, not fluorescent lime green or an insipid green.

c) The banner says The Handset Bazaar is open........... for buying mobiles for cash $$$ (we need people to know we BUY used/damaged phones)

d) We love colour either solid colour or looks like it has been coloured in on our dark background. Open to white or pastel background versions refer to attached coffee file.
We like Chromavell Orange 021,Haute Red,Dazzling Blue, Cyan Blue, Beetroot Purple, Island Green.
e) How it works – underneath this title put Our deal …………. It’s easy as…………..quote, post, get paid!!!
Quote – first circle hand drawn icon showing mobile phone & $ sign. Underneath it says .....Obtain Quote for Model & Condition
Post – second circle hand drawn icon show parcel. Underneath it says Free Post
Paid – third circle hand drawn icon showing large $ sign. Underneath it says Payment in Two Days
Plans - is swapped for wording- Get Market Quote with a large button which says GO or CLICK HERE (they click on the button & it takes them to the next page)
f) FAQ
Allow for six FAQ’s we will forward correct content to you for final design layout.

g) About Us
Please allow about a paragraph of text here, we will forward correct content to you for final design layout.
h) Contact Us
At the bottom where normal website have ………. home, contact details, blog, etc, please only put Email us & Call us, then social media icons for QV, Work Nest and Chirpel

I) LOGO We don’t have one yet, just put The Handset Bazaar at the top & it needs to be large sized font ................we are new and we need to push our name
If you are not clear on our vision ..........please email me and I will reply very quickly.
Thank you for taking the time to read & understand & get us:)

Target Market(s)

20-45 years any body with a spare smart phone that is lying around and they can get cash for. Target market could be slightly older to 50 but focus of 20-40's

Industry/Entity Type

Business

Number of Pages Required

3 page

Font styles to use
Other font styles liked:
• handwritten font or typewriter font

Requirements
Must have
• Read only attached files dated 4 March, tech error with other files, being removed.
• 1 Layout design of Sketch Flock – rtlbenoviqs #7132809
• 2 Hand drawn icons - refer to files
• 3 White font needs to look like hand written refer to heronandfig.com.au or typewriter font - large size font
• 4 Main colours are Black or dark background, green with white text, preference is hand drawn font. The three circles for quote, post & pay with hand drawn icons can be any colour ...... Purple for quote, orange for post & green for paid
• 5 Big green button underneath 3 circles quote/post/pay - customers click on big button to get instant quote
Nice to have
• Coloured in hand drawings as per file
• Great Hand drawings coloured in
Should not have
• NO template designs so it look like you just put some text & a photo. Don't fill the page with mobile phones, one or two is ok, mobile phone pictures date so fast.
• Cartoons

```html
<!DOCTYPE html>
<html lang="en">
<head>
<meta charset="utf-8">
<title>The Handset Bazaar</title>
<link rel="stylesheet" href="https://fonts.googleapis.com/css2?family=Special+Elite&family=Roboto+Slab:wght@400;700&family=Open+Sans:wght@400;700&display=swap">
<style>
:root{
  --board:#2b2e34;
  --board-dark:#1c1e22;
  --green:#0e9a5b;
  --white:#ffffff;
  --ink:#2f3a33;
  --circle-rim:#5a5a5a;
  --circle-fill:#ececec;
  --sky:#3ab3e6;
  --banner-a:#5b6e86;
  --banner-b:#b46a2c;
}
*{margin:0;padding:0;box-sizing:border-box}
html,body{width:1200px;height:2250px;overflow:hidden}
body{
  position:relative;
  background:radial-gradient(ellipse at 50% 40%,#3a3d44 0%,var(--board) 45%,var(--board-dark) 100%);
  color:var(--white);
  font-family:"Open Sans",Arial,sans-serif;
}
.abs{position:absolute}
.typewriter{font-family:"Special Elite","Courier New",monospace;font-weight:400}
.slab{font-family:"Roboto Slab",Georgia,serif;font-weight:400}

/* header */
.site-header{left:0;top:0;width:1200px;height:132px;background:linear-gradient(#1f2125,#33363c)}
.brand{left:146px;top:38px;font-size:46px;color:var(--green);letter-spacing:1px;white-space:nowrap}
.brand-mid{color:var(--white)}
.header-mail{left:745px;top:52px;display:flex;align-items:center;gap:14px;font-size:18px}

/* banner */
.banner{left:0;top:132px;width:1200px;height:516px;
  background:linear-gradient(115deg,var(--banner-a) 0%,#8a8a8a 45%,var(--banner-b) 62%,#6f7c8c 100%)}
.device-shot{left:188px;top:180px;width:210px;height:413px;border-radius:34px;
  background:linear-gradient(#f4f4f4,#d9d9d9)}
.device-screen{left:204px;top:230px;width:180px;height:320px;
  background:linear-gradient(#1f1f1f 0%,#0e9a5b 35%,#0e9a5b 80%,#1f1f1f 100%)}
.banner-title{left:483px;top:292px;width:585px;height:203px;background:rgba(20,20,24,.72);
  text-align:right;padding:14px 12px 0 0;font-size:40px;line-height:62px;letter-spacing:1px;white-space:nowrap}

/* how it works */
.how{left:132px;top:648px;width:936px;height:545px;background:var(--green)}
.how-title{left:0;top:662px;width:1200px;text-align:center;font-size:31px}
.how-deal{left:0;top:704px;width:1200px;text-align:center;font-size:25px;color:var(--ink);white-space:nowrap}
.step-label{width:260px;text-align:center;font-size:30px}
.step-circle{width:192px;height:192px;border-radius:50%;border:7px solid var(--circle-rim);background:var(--circle-fill);
  display:flex;align-items:center;justify-content:center;box-shadow:0 22px 18px -14px rgba(0,0,0,.35)}
.step-icon{width:104px;height:104px;border-radius:50%;background:radial-gradient(#6a6a6a,#3b3b3b)}
.step-caption{width:300px;text-align:center;font-size:23px;line-height:37px}

/* quote cta */
.cta-text{left:290px;top:1230px;font-size:34px;letter-spacing:1px;white-space:nowrap}
.go-button{left:758px;top:1205px;width:104px;height:104px;border-radius:50%;border:4px solid var(--sky);
  display:flex;align-items:center;justify-content:center;font-family:"Special Elite","Courier New",monospace;font-size:34px;color:var(--white);text-decoration:none}

/* faq */
.faq{left:132px;top:1308px;width:936px;height:552px;background:var(--green)}
.faq-title{left:146px;top:1334px;font-size:30px;letter-spacing:1px}
.faq-item{width:340px}
.faq-q{font-size:14px;line-height:20px;padding-left:21px;position:relative;font-family:Arial,sans-serif;white-space:nowrap}
.faq-q::before{content:"";position:absolute;left:-13px;top:1px;width:18px;height:18px;border-radius:50%;border:5px solid var(--white);background:var(--green)}
.faq-rule{height:2px;margin:6px 0 10px 21px;width:314px;background:linear-gradient(90deg,rgba(255,255,255,0),rgba(220,230,150,.7),rgba(255,255,255,0))}
.faq-a{font-size:13px;line-height:17px;padding-left:21px;font-family:Arial,sans-serif}

/* about */
.about-title{left:142px;top:1877px;font-size:27px;letter-spacing:1px}
.about-text{left:142px;top:1932px;width:920px;font-size:13.4px;line-height:20px}
.about-text p+p{margin-top:2px}
.read-more{left:940px;top:2082px;font-size:18px;color:var(--white);text-decoration:none;border-bottom:2px solid rgba(255,255,255,.6)}

/* footer */
.site-footer{left:132px;top:2130px;width:936px;height:120px;background:var(--green)}
.contact-title{left:146px;top:2138px;font-size:18px;font-weight:700;font-family:"Roboto Slab",Georgia,serif}
.contact-line{left:146px;display:flex;align-items:center;gap:14px;font-size:18px;font-family:"Roboto Slab",Georgia,serif}
.footer-brand{left:0;top:2158px;width:1200px;text-align:center;font-size:28px;color:#dff3e6}
.copyright{left:0;top:2206px;width:1200px;text-align:center;font-size:11px}
.social-title{left:873px;top:2138px;font-size:18px;font-weight:700;font-family:"Roboto Slab",Georgia,serif;white-space:nowrap}
.social{width:44px;height:44px;border-radius:6px;background:#f1f1f1;box-shadow:2px 3px 0 rgba(0,0,0,.35)}
</style>
</head>
<body>

<header class="site-header abs"></header>
<div class="brand abs typewriter">The <span class="brand-mid">Handset</span> Bazaar</div>
<div class="header-mail abs">
  <svg width="26" height="22" viewBox="0 0 26 22"><rect x="1" y="1" width="24" height="20" rx="4" fill="#fff"/><path d="M5 7l8 6 8-6" fill="none" stroke="#333" stroke-width="2"/></svg>
  <span>hello@handsetbazaar.example</span>
</div>

<section class="banner abs" role="img" aria-label="Stock market chart backdrop with a rising arrow"></section>
<div class="device-shot abs" role="img" aria-label="Smartphone showing the website on its screen"></div>
<div class="device-screen abs" role="img" aria-label="Website preview on the phone screen"></div>
<h1 class="banner-title abs typewriter">THE HANDSET BAZAAR IS<br>OPEN FOR BUYING<br>MOBILES FOR CASH</h1>

<section class="how abs"></section>
<h2 class="how-title abs typewriter">HOW IT WORKS</h2>
<p class="how-deal abs typewriter">Our deal... Its as...... Quote, Post, Get Paid <b>$$$</b></p>
<svg class="abs" style="left:220px;top:668px" width="260" height="120" viewBox="0 0 260 120">
  <path d="M255 12 C180 0 60 10 30 40 C12 58 10 80 12 100" fill="none" stroke="#fff" stroke-width="2"/>
  <path d="M2 92 L12 108 L22 92" fill="none" stroke="#fff" stroke-width="2"/>
</svg>

<div class="step-label abs typewriter" style="left:126px;top:784px">Quote</div>
<div class="step-label abs typewriter" style="left:468px;top:784px">Post</div>
<div class="step-label abs typewriter" style="left:803px;top:784px">Paid</div>

<div class="step-circle abs" style="left:160px;top:840px"><div class="step-icon" role="img" aria-label="Hand drawn phone with dollar sign"></div></div>
<div class="step-circle abs" style="left:502px;top:840px"><div class="step-icon" role="img" aria-label="Hand drawn parcel"></div></div>
<div class="step-circle abs" style="left:837px;top:840px"><div class="step-icon" role="img" aria-label="Hand drawn money bag"></div></div>

<svg class="abs" style="left:383px;top:914px" width="92" height="44" viewBox="0 0 92 44"><path d="M2 14 H58 V3 L89 22 L58 41 V30 H2 Z" fill="none" stroke="#fff" stroke-width="2"/></svg>
<svg class="abs" style="left:723px;top:914px" width="92" height="44" viewBox="0 0 92 44"><path d="M2 14 H58 V3 L89 22 L58 41 V30 H2 Z" fill="none" stroke="#fff" stroke-width="2"/></svg>

<p class="step-caption abs slab" style="left:106px;top:1062px">Obtain Quote For<br>Model &amp; Condition</p>
<p class="step-caption abs slab" style="left:448px;top:1062px">Free Post</p>
<p class="step-caption abs slab" style="left:783px;top:1062px">Payment Into Your<br>Bank Account Within<br>Two Days</p>

<div class="cta-text abs typewriter">Get Market Quote</div>
<svg class="abs" style="left:644px;top:1234px" width="96" height="44" viewBox="0 0 96 44"><path d="M2 14 H62 V3 L93 22 L62 41 V30 H2 Z" fill="none" stroke="#fff" stroke-width="2"/></svg>
<a class="go-button abs" href="#quote">GO</a>

<section class="faq abs"></section>
<h2 class="faq-title abs typewriter">Frequently Asked Questions</h2>
<svg class="abs" style="left:132px;top:1388px" width="936" height="14" viewBox="0 0 936 14"><path d="M10 10 C250 4 520 2 934 6" fill="none" stroke="#fff" stroke-width="2.5"/></svg>

<div class="faq-item abs" style="left:166px;top:1418px"><p class="faq-q">Lorem ipsum is the dummy text of the industry ?</p><div class="faq-rule"></div><p class="faq-a">Lorem ipsum dolor sit amet, consectetuer adipiscing elit, sed diam nonummy nibh euismod tincidunt ut laoreet dolore magna aliquam erat volutpat. Ut wisi enim ad minim veniam,</p></div>
<div class="faq-item abs" style="left:640px;top:1418px"><p class="faq-q">Lorem ipsum is the dummy text of the industry ?</p><div class="faq-rule"></div><p class="faq-a">Lorem ipsum dolor sit amet, consectetuer adipiscing elit, sed diam nonummy nibh euismod tincidunt ut laoreet dolore magna aliquam erat volutpat. Ut wisi enim ad minim veniam,</p></div>
<div class="faq-item abs" style="left:166px;top:1568px"><p class="faq-q">Lorem ipsum is the dummy text of the industry ?</p><div class="faq-rule"></div><p class="faq-a">Lorem ipsum dolor sit amet, consectetuer adipiscing elit, sed diam nonummy nibh euismod tincidunt ut laoreet dolore magna aliquam erat volutpat. Ut wisi enim ad minim veniam,</p></div>
<div class="faq-item abs" style="left:640px;top:1568px"><p class="faq-q">Lorem ipsum is the dummy text of the industry ?</p><div class="faq-rule"></div><p class="faq-a">Lorem ipsum dolor sit amet, consectetuer adipiscing elit, sed diam nonummy nibh euismod tincidunt ut laoreet dolore magna aliquam erat volutpat. Ut wisi enim ad minim veniam,</p></div>
<div class="faq-item abs" style="left:166px;top:1718px"><p class="faq-q">Lorem ipsum is the dummy text of the industry ?</p><div class="faq-rule"></div><p class="faq-a">Lorem ipsum dolor sit amet, consectetuer adipiscing elit, sed diam nonummy nibh euismod tincidunt ut laoreet dolore magna aliquam erat volutpat. Ut wisi enim ad minim veniam,</p></div>
<div class="faq-item abs" style="left:640px;top:1718px"><p class="faq-q">Lorem ipsum is the dummy text of the industry ?</p><div class="faq-rule"></div><p class="faq-a">Lorem ipsum dolor sit amet, consectetuer adipiscing elit, sed diam nonummy nibh euismod tincidunt ut laoreet dolore magna aliquam erat volutpat. Ut wisi enim ad minim veniam,</p></div>

<h2 class="about-title abs typewriter">About The Handset Bazaar</h2>
<svg class="abs" style="left:138px;top:1918px" width="926" height="8" viewBox="0 0 926 8"><path d="M2 5 C300 2 600 6 924 3" fill="none" stroke="#9a9ca0" stroke-width="2"/></svg>
<div class="about-text abs">
  <p>Lorem ipsum dolor sit amet, consectetuer adipiscing elit, sed diam nonummy nibh euismod tincidunt ut laoreet dolore magna aliquam erat volutpat. Ut wisi enim ad minim veniam.</p>
  <p>quis nostrud exerci tation ullamcorper suscipit lobortis nisl ut aliquip ex ea commodo consequat. Duis autem vel eum iriure dolor in hendrerit in vulputate velit esse molestie consequat, vel illum dolore eu feugiat nulla facilisat vero eros et accumsan et iusto odio dignissim qui blandiraesent luptatum zzril delenit augue duis dolore te feugait nulla facilisi.Lorem ipsum dolor sit amet, consectetuer adipiscing elit, sed diam nonumy nibh euismod tincidunt ut laoreet dolore magna aliquam erat volutpat. Ut wisi enim ad minim veniam, quis nostrud exerci tation ullamcorper suscipit lobortis nisl ut aliquip ex ea commodo consequat lorem is the dummy text of the industry.</p>
</div>
<a class="read-more abs typewriter" href="#about">READ MORE</a>

<footer class="site-footer abs"></footer>
<div class="contact-title abs">Contact Details</div>
<div class="contact-line abs" style="top:2166px">
  <svg width="28" height="28" viewBox="0 0 28 28"><rect x="1" y="1" width="26" height="26" rx="5" fill="#f1f1f1"/><path d="M9 6c-2 1-3 3-2 6 1 4 5 8 9 10 3 1 5 0 6-2l-3-3-2 2c-2-1-4-3-5-5l2-2z" fill="#333"/></svg>
  <span>123-456-7890</span>
</div>
<div class="contact-line abs" style="top:2204px">
  <svg width="28" height="28" viewBox="0 0 28 28"><rect x="1" y="1" width="26" height="26" rx="5" fill="#f1f1f1"/><rect x="6" y="8" width="16" height="12" fill="none" stroke="#333" stroke-width="2"/><path d="M6 8l8 6 8-6" fill="none" stroke="#333" stroke-width="2"/></svg>
  <span>hello@handsetbazaar.example</span>
</div>
<div class="footer-brand abs typewriter">The Handset Bazaar</div>
<div class="copyright abs">2015 THE HANDSET BAZAAR. All Rights Reserved</div>
<div class="social-title abs">Stay Connected with</div>
<div class="social abs" style="left:893px;top:2178px" role="img" aria-label="QV"></div>
<div class="social abs" style="left:950px;top:2178px" role="img" aria-label="Chirpel"></div>
<div class="social abs" style="left:1007px;top:2178px" role="img" aria-label="Work Nest"></div>

</body>
</html>
```